Corvanlit.media

I need a full page PSD made (desktop and mobile view) with a layout similar to what I have in my text file, but a smooth flowing, good looking design. Only take my text file as an idea of order things show flow. I have taken my exact steps from the text file, put them together, and it did not look good, which is why I am seeking a professional design.

```html
<!DOCTYPE html>
<html lang="en">
<head>
<meta charset="utf-8">
<title>Corvanlit.media — Reviews and Text Marketing</title>
<link rel="stylesheet" href="https://fonts.googleapis.com/css2?family=Poppins:wght@400;500;600;700;800&display=swap">
<style>
:root{
  --stage:#2b2b2b;
  --blue:#1f6ff2;
  --blue-dark:#0f4fc9;
  --blue-deep:#0b3a99;
  --ink:#1b2440;
  --muted:#6a7591;
  --pale:#eef4ff;
  --white:#ffffff;
  --green:#22b45a;
}
*{box-sizing:border-box;margin:0;padding:0}
html,body{width:1200px;height:2396px;overflow:hidden;background:var(--stage);font-family:"Poppins",sans-serif;color:var(--ink)}
.artboard{position:absolute;background:var(--white);overflow:hidden}
.desktop{left:160px;top:60px;width:640px;height:2252px}
.mobile{left:820px;top:60px;width:240px;height:1912px}
.sec{position:absolute;left:0;width:100%}
.brand{font-weight:700;color:var(--ink);display:flex;align-items:center;gap:6px}
.brand .dot{width:10px;height:10px;border-radius:50%;background:var(--blue)}
.ph{border-radius:6px}
/* desktop */
.d-header{top:0;height:52px;display:flex;align-items:center;justify-content:space-between;padding:0 48px;font-size:15px}
.d-nav{display:flex;gap:18px;font-size:7px;font-weight:600;color:var(--ink);letter-spacing:.5px}
.d-hero{top:52px;height:260px;background:var(--pale)}
.d-hero h1{position:absolute;left:48px;top:62px;width:270px;font-size:25px;line-height:1.18;color:var(--blue);font-weight:700}
.d-hero p{position:absolute;left:48px;top:160px;font-size:17px;font-weight:600}
.d-hero .ph{position:absolute;right:40px;top:34px;width:250px;height:176px;background:linear-gradient(135deg,#7b5b45,#c9a27a 55,#3b4a66)}
.d-hero .card{position:absolute;right:90px;top:176px;width:150px;height:44px;background:var(--white);border-radius:6px;box-shadow:0 4px 12px rgba(0,0,0,.15);padding:8px 10px;font-size:8px;font-weight:600}
.d-hero .card small{display:block;font-weight:400;color:var(--muted);font-size:6px}
.d-how{top:300px;height:720px}
.heading{text-align:center;color:var(--white)}
.heading h2{font-size:20px;font-weight:700}
.heading span{font-size:8px;font-weight:500}
.step-label{font-size:13px;font-weight:700}
.step-label u{text-decoration:none;display:block;width:24px;height:2px;background:currentColor;margin:3px 0 6px}
.step-title{font-size:11px;font-weight:600;line-height:1.3}
.step-text{font-size:6px;line-height:1.5;opacity:.85;margin-top:6px}
.onblue{color:var(--white)}
.d-step1{position:absolute;left:48px;top:186px;width:200px}
.d-step1-img{position:absolute;left:320px;top:186px;width:200px;height:120px;background:linear-gradient(135deg,#1c2230,#5a5148 60%,#c8c0b0)}
.d-step2-img{position:absolute;left:58px;top:330px;width:150px;height:300px;border-radius:22px;background:linear-gradient(180deg,#f3f5f9,#dde3ee)}
.d-step2{position:absolute;left:340px;top:450px;width:220px}
.d-step3{top:1010px;height:230px}
.d-step3 .txt{position:absolute;left:48px;top:86px;width:190px;color:var(--blue)}
.d-step3 .ph{position:absolute;left:330px;top:40px;width:230px;height:150px;background:linear-gradient(180deg,#e7efff,#c6d8fb);box-shadow:0 6px 16px rgba(0,0,0,.12)}
.d-tm{top:1250px;height:500px}
.d-tm .heading{position:absolute;top:40px;width:100%;color:var(--blue-dark)}
.d-tm .heading span{color:var(--ink)}
.d-tm .ph{position:absolute;left:150px;top:100px;width:340px;height:200px;background:linear-gradient(135deg,#c7d3e6,#8aa2c8 50%,#e7c9a9)}
.d-circles{position:absolute;top:340px;left:0;width:100%;display:flex;justify-content:space-around;padding:0 60px}
.circ{width:130px;text-align:center;color:var(--white)}
.circ b{display:flex;align-items:center;justify-content:center;width:40px;height:40px;border-radius:50%;background:var(--white);color:var(--blue);font-size:18px;margin:0 auto 8px;border:3px solid #9cc0ff}
.circ p{font-size:6.5px;line-height:1.5}
.d-price{top:1760px;height:340px;background:linear-gradient(180deg,var(--blue) 0%,var(--blue-dark) 100%)}
.price-bg{position:absolute;right:0;top:0;width:60%;height:100%;background:linear-gradient(90deg,rgba(31,111,242,0),rgba(90,130,200,.55))}
.d-price .heading{position:absolute;top:34px;width:100%}
.price-card{position:absolute;background:var(--white);border-radius:8px;box-shadow:0 8px 20px rgba(0,0,0,.2);text-align:center;color:var(--ink)}
.d-price .price-card{left:240px;top:120px;width:160px;height:200px;padding:14px 16px}
.amt{font-size:28px;font-weight:800;color:var(--blue)}
.amt sup{font-size:12px}.amt small{font-size:9px;font-weight:500;color:var(--muted)}
.price-card .per{font-size:6px;color:var(--muted);margin-bottom:8px}
.feat{list-style:none;text-align:left;font-size:6.5px;line-height:2}
.feat li{display:flex;align-items:center;gap:5px}
.feat li::before{content:"";width:7px;height:7px;border-radius:50%;background:var(--blue)}
.btn{display:inline-block;background:var(--green);color:var(--white);font-size:7px;font-weight:600;padding:4px 16px;border-radius:10px;margin-top:8px}
.d-foot{top:2100px;height:152px;text-align:center}
.d-foot .brand{justify-content:center;font-size:16px;margin-top:38px}
.foot-links{display:flex;justify-content:center;gap:16px;font-size:7px;margin-top:14px;font-weight:500}
.copy{font-size:6px;color:var(--muted);margin-top:10px}
/* mobile */
.m-header{top:0;height:30px;display:flex;align-items:center;justify-content:space-between;padding:0 12px;font-size:9px}
.burger{width:12px;height:9px;border-top:2px solid var(--ink);border-bottom:2px solid var(--ink);position:relative}
.burger::after{content:"";position:absolute;left:0;right:0;top:1.5px;height:2px;background:var(--ink)}
.m-hero{top:30px;height:110px;background:var(--pale);padding:12px}
.m-hero h1{font-size:11px;color:var(--blue);line-height:1.2;width:110px}
.m-hero p{font-size:8px;font-weight:600;margin-top:5px}
.m-hero .ph{position:absolute;right:10px;top:14px;width:100px;height:76px;background:linear-gradient(135deg,#7b5b45,#c9a27a 55,#3b4a66)}
.m-how{top:140px;height:820px;background:var(--blue);padding:20px 14px;color:var(--white)}
.m-how .heading h2{font-size:12px}
.m-how .heading span{font-size:6px}
.m-block{margin-top:16px}
.m-block .step-label{font-size:9px}
.m-block .step-title{font-size:8px}
.m-block .step-text{font-size:5px}
.m-block .ph{height:90px;margin-top:8px}
.m-tm{top:960px;height:390px;padding:20px 14px}
.m-tm .heading{color:var(--blue-dark)}
.m-tm .heading h2{font-size:12px}.m-tm .heading span{font-size:6px;color:var(--ink)}
.m-tm .ph{height:100px;margin-top:10px;background:linear-gradient(135deg,#c7d3e6,#8aa2c8 50%,#e7c9a9)}
.m-circ{margin-top:10px;text-align:center;color:var(--ink)}
.m-circ b{display:flex;align-items:center;justify-content:center;width:26px;height:26px;border-radius:50%;background:var(--blue);color:var(--white);font-size:11px;margin:0 auto 4px}
.m-circ p{font-size:5.5px;line-height:1.45;color:var(--blue-dark)}
.m-price{top:1350px;height:440px;background:linear-gradient(180deg,var(--blue),var(--blue-dark));padding:22px 14px}
.m-price .heading h2{font-size:12px}.m-price .heading span{font-size:6px}
.m-price .price-card{position:relative;margin:16px auto 0;width:130px;padding:12px}
.m-price .amt{font-size:22px}
.m-price .feat{font-size:5.5px}
.m-foot{top:1790px;height:122px;text-align:center}
.m-foot .brand{justify-content:center;font-size:11px;margin-top:22px}
.m-foot .foot-links{font-size:5.5px;gap:8px}
.m-foot .copy{font-size:5px}
</style>
</head>
<body>

<section class="artboard desktop" aria-label="Desktop page">
  <header class="sec d-header">
    <div class="brand"><span class="dot"></span>Corvanlit.media</div>
    <nav class="d-nav"><span>HOME</span><span>REVIEWS</span><span>LOANS</span><span>FOR US</span><span>CONTACT</span></nav>
  </header>

  <div class="sec d-hero">
    <h1>Get 5 Star Reviews and Text Message Marketing</h1>
    <p>All in one tool!</p>
    <div class="ph" role="img" aria-label="Photo of a small shop front"></div>
    <div class="card">New 5 star review<small>Loved the service, highly recommend!</small></div>
  </div>

  <div class="sec d-how">
    <svg width="640" height="720" viewBox="0 0 640 720" style="position:absolute;left:0;top:0">
      <path d="M0 50 C180 0 420 90 640 30 L640 650 C450 720 200 640 0 700 Z" fill="#1f6ff2"/>
    </svg>
    <div class="heading" style="position:absolute;top:100px;width:100%"><h2>How It Works</h2><span>3 Step Review System</span></div>
    <div class="d-step1 onblue">
      <div class="step-label">Step1<u></u></div>
      <div class="step-title">You display an offer near your cash register</div>
      <p class="step-text">Place a small sign by the till inviting customers to text in for a reward.</p>
    </div>
    <div class="d-step1-img ph" role="img" aria-label="Photo of an offer sign on a shop counter"></div>
    <div class="d-step2-img" role="img" aria-label="Phone showing a text message review conversation"></div>
    <div class="d-step2 onblue">
      <div class="step-label">Step2<u></u></div>
      <div class="step-title">Customer starts the review response</div>
      <p class="step-text">They text the keyword and our system asks how their visit went, guiding happy customers to post.</p>
    </div>
  </div>

  <div class="sec d-step3">
    <div class="txt">
      <div class="step-label">Step3<u></u></div>
      <div class="step-title">Your business earns 5 star reviews!</div>
    </div>
    <div class="ph" role="img" aria-label="Screenshot of a review page with star ratings"></div>
  </div>

  <div class="sec d-tm">
    <svg width="640" height="500" viewBox="0 0 640 500" style="position:absolute;left:0;top:0">
      <path d="M0 240 C200 200 420 280 640 230 L640 500 L0 500 Z" fill="#1f6ff2"/>
    </svg>
    <div class="heading"><h2>How It Works</h2><span>Text Marketing System</span></div>
    <div class="ph" role="img" aria-label="Photo of a hand holding a phone with a text message"></div>
    <div class="d-circles">
      <div class="circ"><b>1</b><p>Phone numbers are collected from each happy customer.</p></div>
      <div class="circ"><b>2</b><p>Simply tap the list and send your promo to everyone at once.</p></div>
      <div class="circ"><b>3</b><p>Watch your customers come back through the door!</p></div>
    </div>
  </div>

  <div class="sec d-price">
    <div class="price-bg" role="img" aria-label="Photo of a smiling customer using a phone"></div>
    <div class="heading"><h2>Pricing</h2><span>Simple Price, All the Benefits</span></div>
    <div class="price-card">
      <div class="amt"><sup>$</sup>149<small>/mo</small></div>
      <div class="per">No setup fees</div>
      <ul class="feat"><li>Review Requests</li><li>Text Message Blasts</li><li>Customer Lists</li><li>Review Alerts</li><li>Phone Support</li></ul>
      <span class="btn">Sign Up</span>
    </div>
  </div>

  <footer class="sec d-foot">
    <div class="brand"><span class="dot"></span>Corvanlit.media</div>
    <div class="foot-links"><span>Home</span><span>Pricing</span><span>Login</span><span>Sign Up</span><span>Support</span></div>
    <p class="copy">Copyright 2024 Corvanlit.media</p>
  </footer>
</section>

<section class="artboard mobile" aria-label="Mobile page">
  <header class="sec m-header"><div class="brand"><span class="dot" style="width:7px;height:7px"></span>Corvanlit.media</div><span class="burger"></span></header>
  <div class="sec m-hero">
    <h1>Get 5 Star Reviews and Text Message Marketing</h1>
    <p>All in one tool!</p>
    <div class="ph" role="img" aria-label="Photo of a small shop front"></div>
  </div>
  <div class="sec m-how">
    <div class="heading"><h2>How It Works</h2><span>3 Step Review System</span></div>
    <div class="m-block">
      <div class="step-label">Step1<u></u></div>
      <div class="step-title">You display an offer near your cash register</div>
      <p class="step-text">Place a small sign by the till inviting customers to text in.</p>
      <div class="ph" role="img" aria-label="Photo of an offer sign on a shop counter" style="background:linear-gradient(135deg,#1c2230,#5a5148 60%,#c8c0b0)"></div>
    </div>
    <div class="m-block">
      <div class="step-label">Step2<u></u></div>
      <div class="step-title">Customer starts the review response</div>
      <p class="step-text">They text the keyword and our system guides them to post.</p>
      <div class="ph" role="img" aria-label="Phone showing a text message review conversation" style="height:200px;width:110px;margin:8px auto 0;border-radius:14px;background:linear-gradient(180deg,#f3f5f9,#dde3ee)"></div>
    </div>
    <div class="m-block">
      <div class="step-label">Step3<u></u></div>
      <div class="step-title">Your business earns 5 star reviews!</div>
      <div class="ph" role="img" aria-label="Screenshot of a review page with star ratings" style="background:linear-gradient(180deg,#e7efff,#c6d8fb)"></div>
    </div>
  </div>
  <div class="sec m-tm">
    <div class="heading"><h2>How It Works</h2><span>Text Marketing System</span></div>
    <div class="ph" role="img" aria-label="Photo of a hand holding a phone with a text message"></div>
    <div class="m-circ"><b>1</b><p>Phone numbers are collected from each happy customer.</p></div>
    <div class="m-circ"><b>2</b><p>Tap the list and send your promo to everyone at once.</p></div>
    <div class="m-circ"><b>3</b><p>Watch your customers come back through the door!</p></div>
  </div>
  <div class="sec m-price">
    <div class="heading"><h2>Pricing</h2><span>Simple Price, All the Benefits</span></div>
    <div class="price-card">
      <div class="amt"><sup>$</sup>149<small>/mo</small></div>
      <div class="per">No setup fees</div>
      <ul class="feat"><li>Review Requests</li><li>Text Message Blasts</li><li>Customer Lists</li><li>Review Alerts</li><li>Phone Support</li></ul>
      <span class="btn">Sign Up</span>
    </div>
  </div>
  <footer class="sec m-foot">
    <div class="brand"><span class="dot" style="width:7px;height:7px"></span>Corvanlit.media</div>
    <div class="foot-links"><span>Home</span><span>Pricing</span><span>Login</span><span>Sign Up</span><span>Support</span></div>
    <p class="copy">Copyright 2024 Corvanlit.media</p>
  </footer>
</section>

</body>
</html>
```